Flyer-Design für Service-Plattform für Vor-Ort-Apotheken
Zielgruppe
Wir entwickeln eine Service-Plattform für Vor-Ort-Apotheken, über die Kunden bei Apotheken in der Umgebung online Medikamente kaufen und sich von den Apotheken über einen Livechat beraten lassen können.
Der Flyer soll ein Vertriebsflyer für die Apotheken werden.
Aufgabenstellung
Wir möchten, dass der Flyer vom Design her nicht zu formell wird, sondern möchten auch ein bisschen 'coolen Startup-Charakter' rüberbringen. Der Flyer soll ein zwei-Blatt-Flyer werden.
Ich werde noch einen ersten Entwurf anfügen, der uns leider nicht sehr angesprochen hat, da dieser einfach zu langweilig wirkte.
Die Roadmap im Flyer gefällt uns wirklich sehr gut, der Rest sollte mit Icons versehen werden und eventuell auch prägnante Worte sollten hervorgehoben werden.
Der Blauton ist auch der Ton, den wir auf unserer Website für Header und Footer verwenden, jedoch fehlte uns im ersten Entwurf des Flyers der Grünanteil (z.B. aus unserem Logo).
Falls es noch Fragen oder Anregungen gibt, bitte einfach melden :)!

```html
<!DOCTYPE html>
<html lang="de">
<head>
<meta charset="utf-8">
<title>Apotiva – Flyer</title>
<link rel="stylesheet" href="https://fonts.googleapis.com/css2?family=Open+Sans:ital,wght@0,300;0,400;0,800;1,300;1,800&family=Fira+Sans+Condensed:wght@400&display=swap">
<style>
  :root {
    --blue: #3a9fd2;
    --green: #7cbd35;
    --green-light: #c6df9c;
    --ink: #4a4a56;
    --text: #5c5c66;
    --paper: #ffffff;
    --stage: #e4e4e4;
    --dash: #c9c9c9;
  }
  * { box-sizing: border-box; margin: 0; padding: 0; }
  html, body { width: 1200px; height: 900px; overflow: hidden; }
  body {
    background: var(--stage);
    font-family: "Open Sans", Arial, sans-serif;
    color: var(--text);
    position: relative;
  }
  .flyer {
    position: absolute;
    top: 20px;
    width: 420px;
    height: 860px;
    background: var(--blue);
    overflow: hidden;
    box-shadow: 0 6px 24px rgba(0,0,0,.12);
  }
  .flyer--intro { left: 150px; }
  .flyer--benefits { left: 630px; }

  /* header */
  .masthead {
    position: absolute; left: 0; top: 0;
    width: 320px; height: 125px;
    background: var(--paper);
    border-bottom-right-radius: 70px;
    display: flex; align-items: center; gap: 12px;
    padding-left: 36px;
  }
  .brand {
    font-family: "Open Sans", Arial, sans-serif;
    font-weight: 300;
    font-size: 50px;
    letter-spacing: 2px;
    color: var(--ink);
    line-height: 1;
  }
  .brand-dot {
    width: 26px; height: 26px; border-radius: 50%;
    background: var(--green);
  }
  .tagline {
    position: absolute; left: 36px; top: 140px;
    font-family: "Fira Sans Condensed", Arial, sans-serif;
    font-size: 24px; color: var(--paper);
  }

  /* white body */
  .sheet {
    position: absolute; left: 0; right: 0;
    top: 195px; bottom: 105px;
    background: var(--paper);
    border-radius: 90px 40px 90px 0;
  }
  .heading {
    font-weight: 800;
    text-transform: uppercase;
    color: var(--green);
    letter-spacing: .6px;
    line-height: 1.15;
  }
  .copy {
    font-weight: 300;
    font-size: 11px;
    line-height: 1.45;
    color: var(--text);
  }

  /* intro flyer body */
  .intro { position: absolute; left: 40px; right: 36px; top: 32px; }
  .intro .heading { font-size: 19px; text-align: center; margin-bottom: 10px; }
  .intro .copy { text-align: justify; }
  .roadmap-title { position: absolute; left: 0; right: 0; top: 222px; text-align: center; font-size: 19px; }
  .roadmap { position: absolute; left: 20px; top: 290px; width: 380px; height: 260px; }
  .step { position: absolute; display: flex; align-items: flex-end; gap: 6px; }
  .step-num { font-weight: 800; font-size: 44px; color: var(--green); line-height: .9; }
  .step-label { font-size: 10.5px; text-transform: uppercase; color: var(--ink); line-height: 1.15; }
  .step-icon-slot { border-radius: 10px; background: var(--green-light); }

  .site-url {
    position: absolute; right: 34px; bottom: 34px;
    font-size: 26px; color: var(--paper); letter-spacing: .5px;
  }

  /* benefits flyer */
  .benefits .masthead { width: 330px; }
  .benefit {
    position: absolute; left: 26px; right: 26px; height: 98px;
    display: flex; align-items: center; gap: 16px;
  }
  .benefit--mirror { flex-direction: row-reverse; }
  .benefit-art { flex: 0 0 104px; height: 84px; border-radius: 12px; background: linear-gradient(135deg, var(--green), var(--green-light)); }
  .benefit-chart { flex: 0 0 104px; height: 84px; }
  .benefit-text { flex: 1; }
  .benefit .heading { font-size: 13px; margin-bottom: 5px; }
  .benefit .copy { font-size: 10.5px; }

  .closing { position: absolute; left: 20px; right: 26px; top: 450px; display: flex; gap: 14px; align-items: center; }
  .closing-art { flex: 0 0 140px; height: 100px; border-radius: 14px; background: linear-gradient(135deg, var(--green), var(--green-light)); }
  .closing .heading { font-size: 17px; font-style: italic; margin-bottom: 6px; }
  .closing .copy { font-size: 10px; font-style: italic; }

  .contact {
    position: absolute; right: 34px; bottom: 22px;
    text-align: right; font-style: italic; font-weight: 800;
    font-size: 13px; line-height: 1.25; color: var(--paper);
  }
</style>
</head>
<body>

<!-- Flyer 1: platform introduction -->
<section class="flyer flyer--intro">
  <header class="masthead">
    <span class="brand">Apotiva</span><span class="brand-dot"></span>
  </header>
  <p class="tagline">Klick dich gesund</p>

  <div class="sheet">
    <div class="intro">
      <h2 class="heading">Apotiva ist unsere<br>Serviceplattform</h2>
      <p class="copy">um Ihre lokale Apotheke mit Kunden digital und persönlich zusammenzubringen. Neben einem modernen Shopsystem lässt sich durch umfangreiche Service- und Beratungsfunktionen die Persönlichkeit Ihrer Apotheke erleben. Apotiva bietet eine bedarfgerechte Kundenberatung, Empfehlungs-, Angebots- und Bonus-Systematiken, Notdienst-Suche, digitale Rezept-Vermittlung und mehr.</p>
    </div>

    <h2 class="heading roadmap-title">Kundenzufriedenheit<br>in 4 Schritten</h2>

    <div class="roadmap">
      <svg width="380" height="260" viewBox="0 0 380 260" aria-hidden="true" style="position:absolute;left:0;top:0">
        <path d="M150 40 C 60 50, 30 110, 80 150" fill="none" stroke="var(--dash)" stroke-width="3" stroke-dasharray="7 6"/>
        <path d="M160 150 L 230 140" fill="none" stroke="var(--dash)" stroke-width="3" stroke-dasharray="7 6"/>
        <path d="M330 150 C 330 200, 300 230, 270 240" fill="none" stroke="var(--dash)" stroke-width="3" stroke-dasharray="7 6"/>
        <!-- magnifier -->
        <circle cx="215" cy="30" r="20" fill="none" stroke="var(--green)" stroke-width="6"/>
        <line x1="230" y1="45" x2="256" y2="60" stroke="var(--green)" stroke-width="7" stroke-linecap="round"/>
        <!-- chat bubble -->
        <path d="M40 112 h44 a6 6 0 0 1 6 6 v22 a6 6 0 0 1 -6 6 h-24 l-10 10 v-10 h-10 a6 6 0 0 1 -6 -6 v-22 a6 6 0 0 1 6 -6z" fill="none" stroke="var(--green)" stroke-width="4"/>
      </svg>

      <div class="step" style="left:150px;top:20px">
        <span class="step-num">1</span>
        <span class="step-label" style="margin-left:60px">Apotheke<br>finden</span>
      </div>
      <div class="step" style="left:96px;top:112px;flex-direction:column;align-items:flex-start">
        <div class="step-icon-slot" role="img" aria-label="Icon: Person im Beratungsgespräch" style="width:44px;height:44px"></div>
      </div>
      <div class="step" style="left:70px;top:168px">
        <span class="step-num">2</span>
        <span class="step-label">Beraten<br>lassen</span>
      </div>
      <div class="step" style="left:236px;top:98px">
        <span class="step-num">3</span>
        <div class="step-icon-slot" role="img" aria-label="Icon: Medikamentendose mit Tabletten" style="width:60px;height:52px;align-self:flex-start;margin-top:-20px"></div>
      </div>
      <span class="step-label" style="position:absolute;left:278px;top:150px">Medikamente<br>bestellen</span>
      <div class="step" style="left:200px;top:200px">
        <span class="step-num">4</span>
        <div class="step-icon-slot" role="img" aria-label="Icon: Hand mit Einkaufstasche" style="width:54px;height:54px;align-self:flex-start;margin-top:-30px"></div>
        <span class="step-label">Bestellung<br>abholen</span>
      </div>
    </div>
  </div>

  <p class="site-url">www.apotiva.de</p>
</section>

<!-- Flyer 2: benefits -->
<section class="flyer flyer--benefits benefits">
  <header class="masthead">
    <span class="brand">Apotiva</span><span class="brand-dot"></span>
  </header>
  <p class="tagline">Ihre Vorteile</p>

  <div class="sheet">
    <div class="benefit" style="top:24px">
      <div class="benefit-art" role="img" aria-label="Illustration: Personengruppe mit Sprechblasen"></div>
      <div class="benefit-text">
        <h3 class="heading">Kundenbeziehung stärken</h3>
        <p class="copy">Im Fokus der Serviceplattform steht der Auf- und Ausbau einer langfristigen Beziehung zwischen Kunden und Apotheke.</p>
      </div>
    </div>

    <div class="benefit benefit--mirror" style="top:130px">
      <div class="benefit-art" role="img" aria-label="Illustration: Berg mit Flagge auf dem Gipfel"></div>
      <div class="benefit-text">
        <h3 class="heading">Wettbewerbsfähigkeit ausbauen</h3>
        <p class="copy">Die Wettbewerbsposition gegenüber digitalen Versand-Apotheken wird gestärkt. Apotiva vereint die Vorteile des Versandhandels mit den persönlichen Stärken der lokalen Apotheke.</p>
      </div>
    </div>

    <div class="benefit" style="top:236px">
      <svg class="benefit-chart" viewBox="0 0 104 84" aria-hidden="true">
        <rect x="6" y="44" width="16" height="32" fill="var(--green)"/>
        <rect x="28" y="34" width="16" height="42" fill="var(--green)"/>
        <rect x="50" y="22" width="16" height="54" fill="var(--green)"/>
        <rect x="72" y="10" width="16" height="66" fill="var(--green)"/>
        <path d="M2 80 Q 60 76 96 30" fill="none" stroke="var(--green)" stroke-width="4"/>
        <path d="M88 30 L100 24 L98 38 Z" fill="var(--green)"/>
      </svg>
      <div class="benefit-text">
        <h3 class="heading">Kunden- und Umsatzgewinnung</h3>
        <p class="copy">Die digitale und mobile Kundenansprache erschließt neue Zielgruppen und steigert den Umsatz im Geschäft.</p>
      </div>
    </div>

    <div class="benefit benefit--mirror" style="top:342px">
      <div class="benefit-art" role="img" aria-label="Illustration: startende Rakete"></div>
      <div class="benefit-text">
        <h3 class="heading">Gemeinsam in die Zukunft</h3>
        <p class="copy">Apotiva begleitet die lokale Apotheke in eine digitale Zukunft. Mit Apotiva verbinden sich Partner des E-Health Marktes, um gemeinsam im lokalen Gesundheitsmarkt zu wachsen.</p>
      </div>
    </div>

    <div class="closing">
      <div class="closing-art" role="img" aria-label="Illustration: Gruppe von Personen"></div>
      <div>
        <h3 class="heading">Wachse gemeinsam<br>mit Apotiva</h3>
        <p class="copy">Begleiten Sie uns beim Ausbau unserer Serviceplattform Apotiva und nehmen Sie wesentlichen Einfluss auf die Richtung, die wir gemeinsam einschlagen.</p>
      </div>
    </div>
  </div>

  <address class="contact">0151 2348 8765<br>info@apotiva.de<br>www.apotiva.de</address>
</section>

</body>
</html>
```